Residential & commercial landscaping company

Updated business cards for commercial and landscaping company. We would like to keep out logo, but just need a more updated business card.

```html
<!DOCTYPE html>
<html lang="en">
<head>
<meta charset="utf-8">
<title>TerraVerde Business Card</title>
<link href="https://fonts.googleapis.com/css2?family=Arimo:wght@400;700&family=Tinos:wght@400;700&display=swap" rel="stylesheet">
<style>
  :root {
    --stage: #2b2b2b;
    --card-black: #000000;
    --green-light: #5cc64f;
    --green-mid: #2cb345;
    --green-deep: #06992f;
    --foliage-light: #3bd23a;
    --foliage-dark: #1d9e3c;
    --white: #ffffff;
  }
  * { box-sizing: border-box; margin: 0; padding: 0; }
  html, body { width: 1200px; height: 1015px; overflow: hidden; }
  body {
    background: var(--stage);
    position: relative;
    font-family: "Arimo", Arial, sans-serif;
  }
  .card {
    position: absolute;
    left: 220px;
    width: 760px;
    height: 434px;
    overflow: hidden;
    box-shadow: 0 12px 30px rgba(0,0,0,0.55);
  }
  .card--front { top: 52px; background: var(--card-black); }
  .card--back {
    top: 529px;
    background: linear-gradient(160deg, var(--green-light) 0%, var(--green-mid) 45%, var(--green-deep) 100%);
    color: var(--white);
  }
  .front-brand {
    position: absolute;
    left: 0; right: 0; top: 50%;
    transform: translateY(-50%);
    display: flex;
    align-items: center;
    justify-content: center;
    gap: 22px;
  }
  .front-brand__mark {
    width: 64px; height: 64px;
    border-radius: 50%;
    background: var(--green-mid);
  }
  .front-brand__name {
    font-family: "Arimo", Arial, sans-serif;
    font-weight: 700;
    font-size: 86px;
    color: var(--white);
    letter-spacing: -1px;
  }
  .back-foliage {
    position: absolute;
    right: 0; top: 0;
    width: 350px; height: 100%;
    background: radial-gradient(ellipse at 60% 40%, var(--foliage-light) 0%, var(--foliage-dark) 70%, rgba(29,158,60,0) 100%);
  }
  .back-brand {
    position: absolute;
    left: 56px; top: 70px;
    font-family: "Arimo", Arial, sans-serif;
    font-weight: 700;
    font-size: 62px;
    color: var(--white);
    letter-spacing: -1px;
  }
  .person {
    position: absolute;
    left: 150px; top: 198px;
    font-family: "Tinos", "Times New Roman", serif;
  }
  .person__name { font-weight: 700; font-size: 34px; line-height: 1.1; }
  .person__title { font-size: 30px; line-height: 1.15; }
  .contact {
    position: absolute;
    left: 172px; top: 306px;
    list-style: none;
    font-size: 21px;
    line-height: 1.35;
  }
  .contact li { display: flex; align-items: center; gap: 10px; }
  .contact svg { width: 20px; height: 20px; fill: var(--white); flex: none; }
</style>
</head>
<body>
  <section class="card card--front">
    <div class="front-brand">
      <span class="front-brand__mark"></span>
      <span class="front-brand__name">TerraVerde</span>
    </div>
  </section>

  <section class="card card--back">
    <div class="back-foliage" role="img" aria-label="Stylised green tree canopy with brown branches"></div>
    <div class="back-brand">TerraVerde</div>
    <div class="person">
      <div class="person__name">Daniel Harlow Jr.</div>
      <div class="person__title">Project Manager</div>
    </div>
    <ul class="contact">
      <li>
        <svg viewBox="0 0 24 24" aria-hidden="true"><path d="M6.6 10.8a15.1 15.1 0 0 0 6.6 6.6l2.2-2.2a1 1 0 0 1 1-.25 11.4 11.4 0 0 0 3.6.57 1 1 0 0 1 1 1V20a1 1 0 0 1-1 1A17 17 0 0 1 3 4a1 1 0 0 1 1-1h3.5a1 1 0 0 1 1 1c0 1.25.2 2.450.57 3.57a1 1 0 0 1-.25 1z"/></svg>
        555-014-3862 ext.214
      </li>
      <li>
        <svg viewBox="0 0 24 24" aria-hidden="true"><path d="M7 3h10v4H7zM4 8h16a2 2 0 0 1 2 2v6h-4v5H6v-5H2v-6a2 2 0 0 1 2-2zm4 8v3h8v-3z"/></svg>
        555-019-4457
      </li>
      <li>
        <svg viewBox="0 0 24 24" aria-hidden="true"><path d="M2 5h20v14H2zm2 2v.5l8 5 8-5V7zm0 2.8V17h16V9.8l-8 5z"/></svg>
        dan@TerraVerdeLandscapes.com
      </li>
    </ul>
  </section>
</body>
</html>
```